Cold Brew coffee needs a label design

Im looking for a label design for my cold brew coffee that has a funky street vibe look and feel about it. I'd like to see some neon colours and black - but am open to other ideas something that will pop. I have 2 flavours so would like to be able to change the flavour and ingredients if you can only produce the one label for when I go to print. My bottles are clear with an aluminium lid.

On the label it needs to have:
- my logo
- the flavour. The flavours are 'black' and 'latte'
- ingredients: signature blend brewed coffee & springwater (for black)
- ingredients: signature blend brewed coffee & full cream milk (for latte)
- 200ml
- @brackenwaylnicedbrew

The size of the label has to fit to a maximum 60mm wide x 90mm high - Im open to rectangle or circle. Please find attached some pics and files to help with the design.

Requirements
Must have
• A fig tree similar to picture below.
Nice to have
• Would love if the leave could incorporate these colours. Thank you

```html
<!DOCTYPE html>
<html lang="en">
<head>
<meta charset="utf-8">
<title>Brackenway Ln. Cold Brew Labels</title>
<link rel="stylesheet" href="https://fonts.googleapis.com/css2?family=Bungee&family=Quicksand:wght@500;600&display=swap">
<style>
  :root {
    --canvas: #ffffff;
    --label-ink: #1c1a24;
    --white: #ffffff;
    --black-accent: #a3308f;
    --latte-accent: #f7bd48;
    --city-deep: #3a2a66;
    --city-mid: #6a44a8;
    --city-glow: #e0609e;
    --figure-tone: #c9ad8f;
  }
  * { box-sizing: border-box; margin: 0; padding: 0; }
  html, body {
    width: 1200px; height: 960px; overflow: hidden;
    background: var(--canvas);
  }
  .canvas { position: relative; width: 1200px; height: 960px; }

  .label {
    position: absolute; top: 378px;
    width: 212px; height: 339px;
    background: var(--label-ink);
    color: var(--white);
    font-family: "Quicksand", sans-serif;
    overflow: hidden;
  }
  .label--black { left: 300px; --accent: var(--black-accent); }
  .label--latte { left: 635px; --accent: var(--latte-accent); }

  .label__artwork {
    position: absolute; left: 0; top: 80px; width: 212px; height: 227px;
    background:
      radial-gradient(ellipse 38% 55% at 50% 55%, var(--figure-tone) 0%, rgba(201,173,143,0.35) 55%, transparent 75%),
      linear-gradient(180deg, var(--city-deep) 0%, var(--city-mid) 45%, var(--city-glow) 80%, var(--label-ink) 100%);
  }

  .brand {
    position: absolute; left: 0; right: 0; top: 14px;
    text-align: center;
  }
  .brand__name {
    font-weight: 600; font-size: 27px; line-height: 34px;
    letter-spacing: 0.2px;
  }
  .brand__sub {
    margin-top: 6px;
    font-weight: 600; font-size: 10px; letter-spacing: 4px;
  }

  .flavour {
    position: absolute; left: 0; right: 0; top: 218px;
    text-align: center;
    font-family: "Bungee", sans-serif;
    font-size: 40px; line-height: 48px; letter-spacing: -1px;
    color: var(--accent);
  }

  .ingredients {
    position: absolute; left: 10px; right: 9px; top: 271px; height: 32px;
    border: 1px solid var(--white);
    background: var(--label-ink);
    text-align: center;
    font-weight: 500; font-size: 9.4px; line-height: 13px;
    text-transform: uppercase;
    padding-top: 2px;
  }

  .band {
    position: absolute; left: 0; right: 0; bottom: 0; height: 32px;
    background: var(--accent);
    display: flex; align-items: center; justify-content: space-between;
    padding: 0 7px 0 10px;
    text-transform: uppercase;
  }
  .band__volume { font-weight: 500; font-size: 12.5px; }
  .band__handle { font-weight: 500; font-size: 8.4px; letter-spacing: 0.2px; }
</style>
</head>
<body>
<main class="canvas">

  <section class="label label--black">
    <div class="label__artwork" role="img" aria-label="Illustration of a man in sunglasses and a tuxedo against a purple and pink neon city skyline"></div>
    <header class="brand">
      <div class="brand__name">Brackenway Ln.</div>
      <div class="brand__sub">Cold Brew</div>
    </header>
    <div class="flavour">Black</div>
    <div class="ingredients">Signature Blend<br>Brewed Coffee &amp; Springwater</div>
    <footer class="band">
      <span class="band__volume">200ml</span>
      <span class="band__handle">@brackenwaylnicedbrew</span>
    </footer>
  </section>

  <section class="label label--latte">
    <div class="label__artwork" role="img" aria-label="Illustration of a man in sunglasses and a tuxedo against a purple and pink neon city skyline"></div>
    <header class="brand">
      <div class="brand__name">Brackenway Ln.</div>
      <div class="brand__sub">Cold Brew</div>
    </header>
    <div class="flavour">Latte</div>
    <div class="ingredients">Signature Blend<br>Brewed Coffee &amp; Full Cream Milk</div>
    <footer class="band">
      <span class="band__volume">200ml</span>
      <span class="band__handle">@brackenwaylnicedbrew</span>
    </footer>
  </section>

</main>
</body>
</html>
```